Business Card Design

New business card design

Target Market(s)

Residential & Commercial Property Managers

Industry/Entity Type

Plumbing Services

Contact Information for Business Card

Name - Owen Tredgold, title - Director, Phone Number - 0431 862 507, email - owen@rvb-plumbing.com.au, Company ABN - 73 215 904 386,

Font styles to use
Sans Serif

Colors
0054AA
0677BA
7BADD7
CADEEF
E8F1F8

```html
<!DOCTYPE html>
<html lang="en">
<head>
<meta charset="utf-8">
<title>RVB Plumbing Services – Business Card</title>
<link rel="stylesheet" href="https://fonts.googleapis.com/css2?family=Montserrat:wght@400;500;700&display=swap">
<style>
  :root {
    --page-bg: #f2f1ef;
    --card-bg: #e8e5e0;
    --card-dark: #1f2224;
    --accent-teal: #2596b6;
    --accent-beige: #d9c8ab;
    --ink-dark: #2b2d2f;
    --ink-muted: #55524d;
    --contact-text: #dccdb2;
  }
  * { margin: 0; padding: 0; box-sizing: border-box; }
  html, body {
    width: 1200px;
    height: 1047px;
    overflow: hidden;
    background: var(--page-bg);
    font-family: "Montserrat", sans-serif;
  }
  .business-card {
    position: absolute;
    left: 80px;
    top: 240px;
    width: 1040px;
    height: 567px;
    border-radius: 26px;
    background: var(--card-bg);
    overflow: hidden;
    box-shadow: 0 10px 30px rgba(0,0,0,0.12);
  }
  .card-wave {
    position: absolute;
    inset: 0;
    width: 100%;
    height: 100%;
  }
  .brand {
    position: absolute;
    left: 56px;
    top: 28px;
  }
  .brand-name {
    display: flex;
    align-items: center;
    gap: 18px;
    font-size: 112px;
    font-weight: 500;
    line-height: 1;
    color: var(--ink-dark);
    letter-spacing: 2px;
  }
  .brand-dot {
    width: 26px;
    height: 26px;
    border-radius: 50%;
    background: var(--accent-teal);
    margin-top: 30px;
  }
  .brand-tagline {
    margin-top: 26px;
    font-size: 21px;
    font-weight: 400;
    letter-spacing: 15.5px;
    color: var(--ink-muted);
  }
  .person {
    position: absolute;
    right: 44px;
    top: 50px;
    text-align: right;
  }
  .person-name {
    font-size: 40px;
    font-weight: 700;
    color: var(--accent-teal);
    line-height: 1.1;
  }
  .person-title {
    margin-top: 6px;
    font-size: 25px;
    font-weight: 400;
    color: var(--ink-dark);
  }
  .side-bar {
    position: absolute;
    right: 0;
    top: 56px;
    width: 18px;
    height: 78px;
    background: var(--accent-teal);
  }
  .contact {
    position: absolute;
    right: 44px;
    top: 335px;
    text-align: right;
    color: var(--contact-text);
    font-size: 25px;
    font-weight: 400;
    line-height: 39px;
  }
  .contact-abn { margin-bottom: 36px; }
  .contact-line {
    display: flex;
    justify-content: flex-end;
    align-items: center;
    gap: 10px;
  }
  .contact-icon { width: 22px; height: 22px; }
</style>
</head>
<body>
  <div class="business-card">
    <svg class="card-wave" viewBox="0 0 1040 567" preserveAspectRatio="none" aria-hidden="true">
      <path d="M0 462 C 300 500, 480 410, 640 322 C 780 252, 900 238, 1040 250 L1040 567 L0 567 Z" fill="var(--accent-teal)"/>
      <path d="M0 486 C 300 520, 480 430, 640 340 C 780 268, 900 256, 1040 262 L1040 567 L0 567 Z" fill="var(--accent-beige)"/>
      <path d="M0 494 C 300 528, 480 438, 640 348 C 780 276, 900 264, 1040 268 L1040 567 L0 567 Z" fill="var(--card-dark)"/>
    </svg>

    <div class="brand">
      <div class="brand-name"><span>rvb</span><span class="brand-dot"></span></div>
      <div class="brand-tagline">plumbing services</div>
    </div>

    <div class="person">
      <div class="person-name">Owen Tredgold</div>
      <div class="person-title">Director</div>
    </div>
    <div class="side-bar"></div>

    <div class="contact">
      <div class="contact-abn">Company ABN<br>- 73 215 904 386</div>
      <div class="contact-line">
        <span>0431 862 507</span>
        <svg class="contact-icon" viewBox="0 0 24 24" aria-hidden="true">
          <path d="M6.6 10.8a15.1 15.1 0 0 0 6.6 6.6l2.2-2.2a1 1 0 0 1 1-.25 11.4 11.4 0 0 0 3.6.57 1 1 0 0 1 1 1V20a1 1 0 0 1-1 1A17 17 0 0 1 3 4a1 1 0 0 1 1-1h3.5a1 1 0 0 1 1 1c0 1.25.2 2.45.57 3.57a1 1 0 0 1-.25 1z" fill="var(--accent-teal)"/>
        </svg>
      </div>
      <div class="contact-line">
        <span>owen@rvb-plumbing.com.au</span>
        <svg class="contact-icon" viewBox="0 0 24 24" aria-hidden="true">
          <rect x="2" y="5" width="20" height="14" rx="2" fill="var(--accent-teal)"/>
          <path d="M3 6.5l9 6.5 9-6.5" fill="none" stroke="var(--card-dark)" stroke-width="1.6"/>
        </svg>
      </div>
    </div>
  </div>
</body>
</html>
```